Mortgage Broking boutique Business

I’m wanting a revamped look to my existing business card design. I do like the black and silver but happy to have other colours introduced based on your creation. I’ve attached a copy of my current card so you can have a starting point updated details noted brloe. I deal with high net worth individuals so need my card to be sophisticated, classy that gives off a classy vibe

Target Market(s)

High net worth, wealthy

Industry/Entity Type

Mortgage Brokerage

Contact Information for Business Card

Job title: Finance Executive
Phone: +61 7 3862 1197
Mobile: 0431 275 506
Email: marcus@quillbrookcapital.com.au
Web: www.quillbrookcapital.com.au
Address: level 22 Tamberlin House, 48 Mercer Rd Brisbane QLD 4000

Font styles to use
Other font styles liked:
• Helvetica

Colors

Designer to choose colors to be used in the design.

Requirements
Must have
• Use my existing card design as a starting point

```html
<!DOCTYPE html>
<html lang="en">
<head>
<meta charset="utf-8">
<title>Quillbrook Capital – Business Card</title>
<link href="https://fonts.googleapis.com/css2?family=Montserrat:wght@300;400;600&display=swap" rel="stylesheet">
<style>
  :root {
    --backdrop: #1b1b1b;
    --card-dark: #202020;
    --card-light: #e6e6e6;
    --ink-dark: #1e1e1e;
    --ink-light: #e4e4e4;
    --ink-muted: #c9c9c9;
  }
  * { margin: 0; padding: 0; box-sizing: border-box; }
  html, body {
    width: 1200px; height: 1200px; overflow: hidden;
    background: var(--backdrop);
    font-family: "Montserrat", Helvetica, Arial, sans-serif;
  }
  .card {
    position: absolute;
    left: 227px; width: 745px; height: 425px;
    background: var(--card-dark);
  }
  .card--front { top: 135px; display: flex; }
  .card--back { top: 640px; }

  .brand-panel {
    width: 373px; height: 100%;
    background: var(--card-light);
    position: relative;
  }
  .brand {
    position: absolute;
    display: flex; flex-direction: column; align-items: flex-start;
  }
  .brand-panel .brand { left: 91px; top: 84px; }
  .card--back .brand { left: 287px; top: 86px; }
  .brand-mark {
    width: 140px; height: 140px;
    background: currentColor;
    margin-bottom: 26px;
  }
  .brand-name {
    font-weight: 600;
    font-size: 23px;
    line-height: 1.4;
    letter-spacing: 1.5px;
    text-transform: uppercase;
  }
  .brand--dark { color: var(--ink-dark); }
  .brand--light { color: var(--ink-light); }

  .details {
    padding: 88px 0 0 73px;
    color: var(--ink-light);
  }
  .person-name {
    font-weight: 600; font-size: 21px; letter-spacing: 1.8px;
    text-transform: uppercase;
  }
  .person-title {
    font-weight: 300; font-size: 16px; color: var(--ink-muted);
    margin-top: 3px; letter-spacing: 0.4px;
  }
  .address {
    font-weight: 300; font-size: 16px; line-height: 23px;
    margin-top: 42px; color: var(--ink-muted); letter-spacing: 0.3px;
  }
  .contacts { list-style: none; margin-top: 28px; }
  .contacts li {
    display: flex; align-items: center;
    font-weight: 300; font-size: 16px; height: 24px;
    color: var(--ink-muted); letter-spacing: 0.3px;
  }
  .contacts svg {
    width: 14px; height: 14px; margin-right: 11px; flex: none;
    fill: none; stroke: var(--ink-muted); stroke-width: 1.4;
  }
  .contacts svg .solid { fill: var(--ink-muted); stroke: none; }
</style>
</head>
<body>
  <section class="card card--front">
    <div class="brand-panel">
      <div class="brand brand--dark">
        <span class="brand-mark"></span>
        <span class="brand-name">Quillbrook<br>Capital</span>
      </div>
    </div>
    <div class="details">
      <p class="person-name">Marcus Ellery</p>
      <p class="person-title">Finance Executive</p>
      <p class="address">level 22 Tamberlin House,<br>48 Mercer Rd Brisbane QLD 4000</p>
      <ul class="contacts">
        <li>
          <svg viewBox="0 0 14 14"><path class="solid" d="M1 5c0-2 2.5-3 6-3s6 1 6 3v1h-3V5H4v1H1z M3 7h8l1 5H2z"/></svg>
          +61 7 3862 1197
        </li>
        <li>
          <svg viewBox="0 0 14 14"><rect x="3.5" y="1" width="7" height="12" rx="1.2"/><line x1="6" y1="11" x2="8" y2="11"/></svg>
          0431 275 506
        </li>
        <li>
          <svg viewBox="0 0 14 14"><rect x="1" y="3" width="12" height="8.5"/><path d="M1 3l6 5 6-5M1 11.5l4.5-4M13 11.5l-4.5-4"/></svg>
          marcus@quillbrookcapital.com.au
        </li>
        <li>
          <svg viewBox="0 0 14 14"><circle cx="7" cy="7" r="6"/><path d="M1 7h12M7 1c-2.5 3-2.5 9 0 12M7 1c2.5 3 2.5 9 0 12"/></svg>
          www.quillbrookcapital.com.au
        </li>
      </ul>
    </div>
  </section>

  <section class="card card--back">
    <div class="brand brand--light">
      <span class="brand-mark"></span>
      <span class="brand-name">Quillbrook<br>Capital</span>
    </div>
  </section>
</body>
</html>
```